Nail salon window signage design

We need new signage to be designed for our existing nail salon. The sign will be a large sticker that will stick onto the glass window at the front.

Some of the services we provide are:
Manicures
Pedicures
Velora Gel Builder
Acrylic Nails
KVT
Brenlux
Gel Polish
You may wish to have our services listed on the sign but is not compulsory.

I have also attached our logo which can be used on the sign but is not compulsory.

I have also attached a photo of the front of our salon and the sign will be where I have outlined in yellow.

The size of the sign will be 119cm wide and 170cm high.

I am open to any nice classy design you can think of.

```html
<!DOCTYPE html>
<html lang="en">
<head>
<meta charset="utf-8">
<title>Linden Crest Nails – Window Sign</title>
<link rel="stylesheet" href="https://fonts.googleapis.com/css2?family=Lato:wght@400&display=swap">
<style>
  :root {
    --page: #ffffff;
    --sand-light: #f2e3d3;
    --sand-mid: #ead6c0;
    --sand-edge: #d5b794;
    --gold: #c5ad7b;
    --gold-text: #c2a874;
    --maroon: #7a2430;
    --rule: #9a5a4a;
    --skin-light: #ecd8c0;
    --skin-dark: #d3b692;
    --polish-red: #b5303a;
  }
  * { margin: 0; padding: 0; box-sizing: border-box; }
  html, body {
    width: 910px;
    height: 1200px;
    overflow: hidden;
    background: var(--page);
  }
  .canvas {
    position: relative;
    width: 910px;
    height: 1200px;
    background: var(--page);
    font-family: "Lato", sans-serif;
  }
  .sign {
    position: absolute;
    left: 136px;
    top: 144px;
    width: 638px;
    height: 912px;
    overflow: hidden;
    background: radial-gradient(ellipse 62% 60% at 50% 48%,
      var(--sand-light) 0%, var(--sand-light) 55%, var(--sand-mid) 75%, var(--sand-edge) 100%);
  }
  .brand-name {
    position: absolute;
    left: 0;
    width: 100%;
    top: 160px;
    text-align: center;
    font-size: 44px;
    line-height: 1.2;
    font-weight: 400;
    letter-spacing: 0.04em;
    color: var(--maroon);
  }
  .polish-bottle {
    position: absolute;
    left: 0;
    top: 236px;
    width: 170px;
    height: 80px;
    border-radius: 0 40px 40px 0;
    background: linear-gradient(90deg, var(--maroon) 0%, var(--polish-red) 100%);
    opacity: 0.85;
  }
  .services-heading {
    position: absolute;
    left: 199px;
    top: 292px;
    font-size: 18px;
    line-height: 1;
    font-weight: 400;
    letter-spacing: 0.92em;
    color: var(--gold-text);
    white-space: nowrap;
  }
  .hand-illustration {
    position: absolute;
    left: 420px;
    top: 500px;
    width: 200px;
    height: 412px;
    border-radius: 100px 100px 0 0;
    background: linear-gradient(180deg, var(--skin-dark) 0%, var(--skin-light) 100%);
  }
  .services-panel {
    position: absolute;
    left: 104px;
    top: 330px;
    width: 430px;
    height: 438px;
    background: var(--gold);
  }
  .service-list {
    list-style: none;
    position: absolute;
    left: 61px;
    top: 29px;
    width: 308px;
  }
  .service-item {
    height: 53px;
    display: flex;
    align-items: center;
    justify-content: center;
    font-size: 20px;
    letter-spacing: 0.2em;
    color: var(--maroon);
    white-space: nowrap;
    border-bottom: 1px solid var(--rule);
  }
  .service-item:last-child { border-bottom: none; }
</style>
</head>
<body>
  <main class="canvas">
    <section class="sign">
      <h1 class="brand-name">Linden Crest Nails</h1>

      <div class="polish-bottle" role="img" aria-label="Illustration of a nail polish bottle with a brush dripping red polish"></div>

      <h2 class="services-heading">SERVICES</h2>

      <div class="hand-illustration" role="img" aria-label="Illustration of an elegant hand with red painted nails holding the services panel"></div>

      <div class="services-panel">
        <ul class="service-list">
          <li class="service-item">MANICURES</li>
          <li class="service-item">PEDICURES</li>
          <li class="service-item">VELORA GEL BUILDER</li>
          <li class="service-item">ACRYLIC NAILS</li>
          <li class="service-item">KVT</li>
          <li class="service-item">BRENLUX</li>
          <li class="service-item">GEL POLISH</li>
        </ul>
      </div>
    </section>
  </main>
</body>
</html>
```